I need 2 flyers designed for my business

Both can be similar in design and will have different purposes. I need an education based flyer and I need a government based flyer. The focus of the flyer will be software on the front and services on the back.
These all need to be 8.5x 11 in dimension (they can be full bleed). I would like to be able to print these out if needed. The design needs to look good with our website > www.brelmark.com

The software details are on the website.

```html
<!DOCTYPE html>
<html lang="en">
<head>
<meta charset="utf-8">
<title>Brelmark Records – Flyers</title>
<link rel="stylesheet" href="https://fonts.googleapis.com/css2?family=Rubik:wght@500;700;800&family=Open+Sans:wght@400;600&display=swap">
<style>
  :root {
    --sky: #17a3dc;
    --olive: #8c7a3a;
    --maroon: #7d1417;
    --crimson: #9e1a1f;
    --deep-red: #5e0c10;
    --paper: #ffffff;
    --backdrop: #e6e6e6;
  }
  html, body {
    margin: 0;
    padding: 0;
    width: 713px;
    height: 1200px;
    overflow: hidden;
    background: var(--backdrop);
  }
  .canvas {
    position: relative;
    width: 713px;
    height: 1200px;
  }
  .flyer {
    position: absolute;
    left: 146px;
    width: 420px;
    height: 544px;
    display: block;
  }
  .flyer--software { top: 43px; }
  .flyer--services { top: 618px; }
  .headline { font-family: "Rubik", sans-serif; font-weight: 800; fill: var(--paper); }
  .brand-name { font-family: "Rubik", sans-serif; font-weight: 700; fill: var(--maroon); }
  .feature-label { font-family: "Rubik", sans-serif; font-weight: 700; fill: var(--maroon); font-size: 13px; }
  .product-name { font-family: "Rubik", sans-serif; font-weight: 700; fill: var(--maroon); font-size: 21px; }
  .service-title { font-family: "Rubik", sans-serif; font-weight: 500; fill: var(--paper); font-size: 21px; }
  .body-copy { font-family: "Open Sans", sans-serif; font-weight: 400; fill: var(--paper); font-size: 9.6px; }
  .contact-copy { font-family: "Open Sans", sans-serif; font-weight: 400; fill: var(--paper); font-size: 9.6px; }
  .icon { fill: var(--paper); }
  .icon-line { fill: none; stroke: var(--paper); stroke-width: 3; stroke-linecap: round; stroke-linejoin: round; }
</style>
</head>
<body>
<main class="canvas">

  <!-- Front: software -->
  <svg class="flyer flyer--software" viewBox="0 0 566 732" xmlns="http://www.w3.org/2000/svg">
    <defs>
      <filter id="pill-shadow" x="-20%" y="-30%" width="140%" height="160%">
        <feDropShadow dx="2" dy="3" stdDeviation="3" flood-color="#000" flood-opacity="0.16"/>
      </filter>
    </defs>
    <rect class="sheet" width="566" height="732" fill="var(--paper)"/>

    <polygon class="hero-band" points="0,0 297,0 404,186 316,374 0,374" fill="var(--sky)"/>
    <polygon class="hero-accent" points="296,374 382,238 401,286 346,374" fill="var(--olive)"/>

    <text class="headline" font-size="41">
      <tspan x="52" y="128">Record</tspan>
      <tspan x="52" y="175">Management</tspan>
      <tspan x="52" y="221">Services &amp;</tspan>
      <tspan x="52" y="267">Software</tspan>
    </text>

    <g class="brand-lockup">
      <circle cx="386" cy="73" r="9" fill="var(--maroon)"/>
      <text class="brand-name" x="402" y="66" font-size="18">BRELMARK</text>
      <text class="brand-name" x="402" y="86" font-size="18">RECORDS</text>
    </g>

    <g class="feature-pills" filter="url(#pill-shadow)" fill="var(--paper)">
      <rect x="95" y="418" width="112" height="50" rx="25"/>
      <rect x="348" y="418" width="118" height="50" rx="25"/>
      <rect x="58" y="504" width="120" height="56" rx="28"/>
      <rect x="394" y="504" width="106" height="50" rx="25"/>
      <rect x="95" y="594" width="112" height="56" rx="28"/>
      <rect x="348" y="594" width="118" height="56" rx="28"/>
    </g>
    <text class="feature-label"><tspan x="111" y="440">Document</tspan><tspan x="111" y="454">Archive</tspan></text>
    <text class="feature-label"><tspan x="366" y="438">HR</tspan><tspan x="366" y="452">Onboarding</tspan></text>
    <text class="feature-label"><tspan x="74" y="519">Electronic</tspan><tspan x="74" y="533">Forms &amp;</tspan><tspan x="74" y="547">Workflows</tspan></text>
    <text class="feature-label" x="412" y="533">eSigning</text>
    <text class="feature-label"><tspan x="111" y="608">Mileage &amp;</tspan><tspan x="111" y="622">Expense</tspan><tspan x="111" y="636">Tracking</tspan></text>
    <text class="feature-label"><tspan x="364" y="609">Scanning &amp;</tspan><tspan x="364" y="623">Database</tspan><tspan x="364" y="637">Conversion</tspan></text>

    <g class="product-badge">
      <circle cx="274" cy="530" r="65" fill="var(--paper)" stroke="var(--maroon)" stroke-width="3"/>
      <text class="product-name" x="274" y="537" text-anchor="middle">LedgerView</text>
    </g>

    <polygon class="footer-olive" points="0,598 56,694 385,694 402,732 0,732" fill="var(--olive)"/>
    <polygon class="footer-sky" points="200,658 493,658 566,732 566,732 402,732 385,694 228,694" fill="var(--sky)"/>
  </svg>

  <!-- Back: services -->
  <svg class="flyer flyer--services" viewBox="0 0 566 732" xmlns="http://www.w3.org/2000/svg">
    <defs>
      <radialGradient id="circuit-glow" cx="50%" cy="55%" r="75%">
        <stop offset="0" stop-color="#b8252b"/>
        <stop offset="0.6" stop-color="var(--crimson)"/>
        <stop offset="1" stop-color="var(--deep-red)"/>
      </radialGradient>
    </defs>
    <rect class="circuit-backdrop" width="566" height="732" fill="url(#circuit-glow)" role="img" aria-label="Red circuit-board pattern background"/>

    <polygon class="brand-banner" points="364,0 550,0 550,146 457,200 364,146" fill="var(--paper)"/>
    <g class="brand-lockup">
      <circle cx="392" cy="84" r="9" fill="var(--maroon)"/>
      <text class="brand-name" x="408" y="76" font-size="18">BRELMARK</text>
      <text class="brand-name" x="408" y="96" font-size="18">RECORDS</text>
    </g>

    <text class="headline" x="44" y="114" font-size="66" font-weight="700">Services</text>
    <text class="body-copy">
      <tspan x="46" y="152">Brelmark Records offers comprehensive records</tspan>
      <tspan x="46" y="165">management services, including secure, offsite document</tspan>
      <tspan x="46" y="178">storage, online document hosting, document conversion services,</tspan>
      <tspan x="46" y="191">and enterprise solutions, for businesses of all sizes.</tspan>
    </text>

    <!-- Software -->
    <g class="service-icon">
      <circle cx="140" cy="275" r="14" class="icon-line" stroke-width="6" stroke-dasharray="5 4"/>
      <circle cx="140" cy="275" r="5" class="icon"/>
      <path class="icon-line" stroke-width="2" d="M156 268 H170 M156 276 H176 M156 284 H170"/>
      <circle cx="172" cy="268" r="2.5" class="icon"/><circle cx="178" cy="276" r="2.5" class="icon"/><circle cx="172" cy="284" r="2.5" class="icon"/>
    </g>
    <text class="service-title" x="149" y="333" text-anchor="middle">Software</text>
    <text class="body-copy" text-anchor="middle">
      <tspan x="149" y="358">Access all of your records – whether</tspan>
      <tspan x="149" y="371">active or inactive – through LedgerView,</tspan>
      <tspan x="149" y="384">our comprehensive records man-</tspan>
      <tspan x="149" y="397">agement software.</tspan>
    </text>

    <!-- Scanning -->
    <g class="service-icon">
      <path class="icon-line" stroke-width="2.5" d="M364 268 L399 256 L434 268 L399 280 Z M364 276 L399 288 L434 276 M364 284 L399 296 L434 284"/>
    </g>
    <text class="service-title" x="399" y="333" text-anchor="middle">Scanning</text>
    <text class="body-copy" text-anchor="middle">
      <tspan x="399" y="358">Rediscover your office space by</tspan>
      <tspan x="399" y="371">letting us store your records offsite.</tspan>
    </text>

    <!-- Storage -->
    <g class="service-icon">
      <rect x="124" y="462" width="48" height="10" class="icon-line" stroke-width="2.5"/>
      <rect x="120" y="474" width="56" height="32" class="icon"/>
      <rect x="141" y="484" width="14" height="4" fill="var(--crimson)"/>
    </g>
    <text class="service-title" x="149" y="550" text-anchor="middle">Storage</text>
    <text class="body-copy" text-anchor="middle">
      <tspan x="149" y="579">Rediscover your office space by</tspan>
      <tspan x="149" y="592">letting us store your records offsite.</tspan>
    </text>

    <!-- Shredding -->
    <g class="service-icon">
      <path class="icon-line" stroke-width="2.5" d="M388 496 V452 H406 L414 460 V496"/>
      <rect x="395" y="472" width="12" height="9" class="icon"/>
      <path class="icon-line" stroke-width="2" d="M397 472 V468 A4 4 0 0 1 405 468 V472"/>
      <rect x="374" y="486" width="52" height="12" rx="2" class="icon-line" stroke-width="2.5"/>
      <path class="icon-line" stroke-width="2" d="M388 502 V514 M394 502 V510 M400 502 V516 M406 502 V510 M412 502 V514"/>
    </g>
    <text class="service-title" x="399" y="550" text-anchor="middle">Shredding</text>
    <text class="body-copy" text-anchor="middle">
      <tspan x="399" y="580">Let us destroy paper-based</tspan>
      <tspan x="399" y="593">documents you no longer need in a</tspan>
      <tspan x="399" y="606">safe, secure, cost-effective manner.</tspan>
    </text>

    <g class="contact-footer">
      <rect x="0" y="654" width="566" height="78" fill="var(--paper)"/>
      <polygon points="0,670 140,670 108,724 0,724" fill="var(--olive)"/>
      <polygon points="140,664 430,664 400,710 110,710" fill="var(--maroon)"/>
      <rect x="0" y="716" width="566" height="16" fill="var(--maroon)"/>
      <polygon points="0,710 566,710 566,716 0,716" fill="var(--olive)"/>
      <text class="contact-copy" text-anchor="middle">
        <tspan x="283" y="688">Phone: (555) 310-2280 | Fax: (555) 310-2291</tspan>
        <tspan x="283" y="701">48 Harbor Lane Millbrook, Ohio 40000</tspan>
      </text>
    </g>
  </svg>

</main>
</body>
</html>
```